New Signage Design Project

Real estate company looking for signage, PowerPoint and stationery branding. Signs will be placed in front of homes and other properties being sold

Name of company is Birch Crest, LLC

Requirements
Must have
• Name of company - Birch Crest, LLC

```html
<!DOCTYPE html>
<html lang="en">
<head>
<meta charset="utf-8">
<title>Birch Crest, LLC — Business Cards</title>
<link rel="stylesheet" href="https://fonts.googleapis.com/css2?family=Montserrat:wght@500;600;700&family=Roboto:wght@400;500&display=swap">
<style>
  :root {
    --backdrop: #e9e7e6;
    --card-dark: #1c2224;
    --card-light: #f2f2f2;
    --ink: #1c2224;
    --ink-soft: #3a4144;
    --accent: #d9414f;
    --white: #ffffff;
  }
  * { box-sizing: border-box; margin: 0; padding: 0; }
  html, body {
    width: 1200px; height: 959px; overflow: hidden;
    background: var(--backdrop);
  }
  .card {
    position: absolute;
    width: 620px; height: 354px;
    border-radius: 3px;
    box-shadow: 0 10px 24px rgba(0,0,0,0.12), 0 2px 4px rgba(0,0,0,0.08);
  }
  .card--front {
    left: 60px; top: 70px;
    background: var(--card-dark);
    display: flex; align-items: center; justify-content: center;
  }
  .card--back {
    left: 520px; top: 500px;
    background: var(--card-light);
    padding: 44px 48px;
  }
  .wordmark {
    display: flex; align-items: center; gap: 16px;
    font-family: "Montserrat", sans-serif;
    font-weight: 600;
    letter-spacing: 0.04em;
    text-transform: uppercase;
  }
  .wordmark__dot {
    border-radius: 50%;
    background: var(--accent);
    flex: none;
  }
  .card--front .wordmark { color: var(--white); font-size: 34px; }
  .card--front .wordmark__dot { width: 30px; height: 30px; }
  .card--back .wordmark { color: var(--ink); font-size: 30px; margin-bottom: 30px; }
  .card--back .wordmark__dot { width: 26px; height: 26px; }

  .person__name {
    font-family: "Montserrat", sans-serif;
    font-weight: 700; font-size: 21px;
    color: var(--ink); text-transform: uppercase; letter-spacing: 0.02em;
  }
  .person__title {
    font-family: "Montserrat", sans-serif;
    font-weight: 600; font-size: 16px;
    color: var(--accent); margin-top: 2px; margin-bottom: 14px;
  }
  .contact { list-style: none; font-family: "Roboto", sans-serif; font-size: 15px; color: var(--ink-soft); }
  .contact__item { display: flex; align-items: center; gap: 8px; line-height: 22px; }
  .contact__icon { width: 13px; height: 13px; flex: none; fill: var(--accent); }
  .address {
    display: flex; gap: 8px; margin-top: 14px;
    font-family: "Roboto", sans-serif; font-size: 15px; color: var(--ink-soft); line-height: 20px;
    font-style: normal;
  }
  .address__company { font-weight: 500; color: var(--ink); font-size: 16px; }
  .address .contact__icon { width: 14px; height: 18px; margin-top: 2px; }
</style>
</head>
<body>
  <section class="card card--front" aria-label="Business card front">
    <div class="wordmark"><span class="wordmark__dot"></span><span>Birch Crest, LLC</span></div>
  </section>

  <section class="card card--back" aria-label="Business card back">
    <div class="wordmark"><span class="wordmark__dot"></span><span>Birch Crest, LLC</span></div>
    <p class="person__name">Martin Ellroy</p>
    <p class="person__title">Managing Director</p>
    <ul class="contact">
      <li class="contact__item">
        <svg class="contact__icon" viewBox="0 0 16 16"><path d="M3 1h3l1.5 4-2 1.3a9 9 0 0 0 4.2 4.2L11 8.5l4 1.5v3a2 2 0 0 1-2 2A12 12 0 0 1 1 3a2 2 0 0 1 2-2z"/></svg>
        GSM +1 555 014 2287
      </li>
      <li class="contact__item">
        <svg class="contact__icon" viewBox="0 0 16 16"><path d="M1 3h14v10H1z M2 4l6 5 6-5" fill="none" stroke="#d9414f" stroke-width="1.6"/></svg>
        info@birchcresthomes.com
      </li>
      <li class="contact__item">
        <svg class="contact__icon" viewBox="0 0 16 16"><circle cx="8" cy="8" r="6.5" fill="none" stroke="#d9414f" stroke-width="1.6"/><path d="M1.5 8h13M8 1.5c-3 3.5-3 9.5 0 13M8 1.5c3 3.5 3 9.5 0 13" fill="none" stroke="#d9414f" stroke-width="1.2"/></svg>
        www.birchcresthomes.com
      </li>
    </ul>
    <address class="address">
      <svg class="contact__icon" viewBox="0 0 14 18"><path d="M7 0a7 7 0 0 1 7 7c0 5-7 11-7 11S0 12 0 7a7 7 0 0 1 7-7zm0 4.5a2.5 2.5 0 1 0 0 5 2.5 2.5 0 0 0 0-5z"/></svg>
      <span>
        <span class="address__company">Birch Crest, LLC</span><br>
        218 Alder Row Avenue,<br>
        Suite 120 Fairhaven USA.
      </span>
    </address>
  </section>
</body>
</html>
```